PowerPoint Design for upcoming Broadcast

I need a PowerPoint design complete with all the templates in PPT, i.e two columns of text, one column of text with adjacent area for image, etc. Per the attached logo. Do not use the gold element in the design. 16x9

Target Market(s)

Business Leaders

Industry/Entity Type

Business Consultant

Font styles to use
Other font styles liked:
• Arial

Colors

Designer to choose colors to be used in the design.

Requirements
Must have
• Crisp clean design. #for each color used.
Nice to have
• An assortment of charts in the ppt color schemes. A military (KVRD) theme.
Should not have
• Gaudy. Flashy. Transitions.

```html
<!DOCTYPE html>
<html lang="en">
<head>
<meta charset="utf-8">
<title>Vanguard Honor Leadership — Presentation Template Overview</title>
<link href="https://fonts.googleapis.com/css2?family=Arimo:wght@400;700&display=swap" rel="stylesheet">
<style>
:root{
  --red:#b50d0d;
  --deep-red:#8f0508;
  --black:#0b0b0b;
  --charcoal:#1c1c1c;
  --gold:#a8874f;
  --canvas:#d4d4d4;
  --ink:#3a3a3a;
}
*{box-sizing:border-box;margin:0;padding:0}
html,body{width:1200px;height:933px;overflow:hidden;background:var(--canvas);font-family:"Arimo",Arial,sans-serif}
.deck{display:grid;grid-template-columns:repeat(5,227px);grid-template-rows:repeat(7,128px);column-gap:10px;row-gap:5px;padding:3px 0 0 12px}
.slide{position:relative;overflow:hidden;background:#fff;color:var(--ink)}
.slide.dark{background:var(--black);color:#fff}
.abs{position:absolute}
.ph{position:absolute}
.mark{position:absolute;right:7px;top:8px;font-size:3.6px;font-weight:700;letter-spacing:.2px;color:var(--red);white-space:nowrap}
.dark .mark,.mark.light{color:#fff}
.mark.big{left:0;right:0;text-align:center;font-size:5px}
.ttl{position:absolute;left:8px;top:7px;font-size:7.2px}
.ttl::after{content:"";position:absolute;left:0;bottom:-3px;width:14px;height:1px;background:var(--red)}
.foot{position:absolute;left:0;right:0;bottom:0;height:5px;background:var(--black);color:#fff;font-size:2.6px;line-height:5px;padding-left:7px;letter-spacing:.1px}
.foot .pg{position:absolute;right:8px;top:0;height:5px;width:18px;background:var(--red);text-align:center}
.t{font-size:3.2px;line-height:1.4;color:var(--ink)}
.dark .t{color:#c9c9c9}
.brand{font-size:6.4px;letter-spacing:.2px}
.sub{font-size:5.4px;line-height:1.3}
.red{color:var(--red)}
.num{font-size:9px;color:var(--black)}
.qm{font-size:12px;font-weight:700;color:var(--red);line-height:1}
.icon{position:absolute;width:9px;height:9px;border-radius:50%;background:var(--red)}
.dot{position:absolute;width:6px;height:6px;border-radius:50%;background:var(--red)}
.sep{position:absolute;height:0;border-top:.5px solid #555}
.price{position:absolute;width:40px}
.price .top{background:var(--black);color:#fff;font-size:6px;text-align:center;padding:4px 0}
.price .lab{background:#fff;color:var(--red);font-size:3.6px;text-align:center;padding:3px 0;border:.5px solid #ccc}
.price .body{border:.5px solid #ccc;border-top:0;padding:3px;text-align:center;height:34px}
.avatar{position:absolute;width:14px;height:14px;border-radius:50%;background:linear-gradient(#9a9a9a,#5a5a5a)}
</style>
</head>
<body>
<main class="deck">

<section class="slide dark">
  <div class="ph" style="inset:0;background:linear-gradient(90deg,#2b2b2b,#121212 35%,#050505 60%,#1d1515)" role="img" aria-label="Executive in a dark suit beside a uniformed officer"></div>
  <div class="abs" style="left:45px;top:34px;width:140px;text-align:center">
    <div class="brand">VANGUARD HONOR LEADERSHIP</div>
    <div class="sub" style="margin-top:29px">Developing Entrepreneurial Leaders<br>and Winning the Small Business War</div>
  </div>
</section>

<section class="slide dark">
  <div class="ph" style="left:0;top:0;bottom:0;width:70px;background:linear-gradient(90deg,#2c2c2c,#0b0b0b)" role="img" aria-label="Executive in a dark suit"></div>
  <div class="abs" style="left:92px;top:42px"><div class="brand">VANGUARD HONOR LEADERSHIP</div>
  <div class="sub" style="margin-top:9px">Developing Entrepreneurial Leaders<br>and Winning the Small Business War</div></div>
</section>

<section class="slide dark">
  <div class="ph" style="left:0;top:0;bottom:0;width:60px;background:linear-gradient(90deg,#262626,#0b0b0b)" role="img" aria-label="Uniformed officer in dress blues"></div>
  <div class="abs" style="left:92px;top:43px"><div class="brand">VANGUARD HONOR LEADERSHIP</div>
  <div class="sub" style="margin-top:9px">Developing Entrepreneurial Leaders<br>and Winning the Small Business War</div></div>
</section>

<section class="slide dark" style="background:#101010">
  <div class="qm abs" style="left:43px;top:39px">“</div>
  <div class="t abs" style="left:58px;top:46px;width:112px">Lorem ipsum dolor sit amet, consectetur adipiscing elit, sed do eiusmod tempor incididunt ut labore et dolore magna aliqua. Ut enim ad minim veniam, quis nostrud exercitation ullamco laboris nisi ut aliquip ex ea commodo consequat.</div>
  <div class="qm abs" style="left:171px;top:68px">”</div>
  <div class="foot">VANGUARD HONOR LEADERSHIP<span class="pg">Page 4</span></div>
</section>

<section class="slide dark">
  <div class="ph" style="left:0;right:0;top:0;height:52px;background:linear-gradient(#3a3a3a,#111)" role="img" aria-label="Empty boardroom with city windows"></div>
  <div class="mark big" style="top:22px">VANGUARD HONOR</div>
  <div class="abs" style="left:0;right:0;top:50px;text-align:center;font-size:7px">WELCOME MESSAGE</div>
  <div class="t abs" style="left:60px;top:66px;width:110px">Lorem ipsum dolor sit amet, consectetur adipiscing elit, sed do eiusmod tempor incididunt ut labore et dolore magna aliqua. Ut enim ad minim veniam, quis nostrud exercitation ullamco laboris nisi ut aliquip ex ea commodo consequat.</div>
  <div class="foot">VANGUARD HONOR LEADERSHIP<span class="pg">Page 5</span></div>
</section>

<section class="slide">
  <div class="mark big" style="top:26px">VANGUARD HONOR</div>
  <div class="abs red" style="left:0;right:0;top:48px;text-align:center;font-size:7px">WELCOME MESSAGE</div>
  <div class="qm abs" style="left:45px;top:64px">“</div>
  <div class="t abs" style="left:60px;top:66px;width:110px">Lorem ipsum dolor sit amet, consectetur adipiscing elit, sed do eiusmod tempor incididunt ut labore et dolore magna aliqua. Ut enim ad minim veniam, quis nostrud exercitation ullamco laboris nisi ut aliquip ex ea commodo consequat.</div>
  <div class="qm abs" style="left:172px;top:80px">”</div>
  <div class="foot">VANGUARD HONOR LEADERSHIP<span class="pg">Page 6</span></div>
</section>

<section class="slide">
  <div class="ttl">Agenda</div><div class="mark">VANGUARD HONOR</div>
  <div class="abs" style="left:34px;top:30px;width:90px">
    <div style="display:flex;gap:4px;margin-bottom:14px"><span class="num">1</span><span style="border-left:1px solid var(--red)"></span><span class="t">Lorem ipsum dolor sit amet,<br>consectetur adipiscing elit</span></div>
    <div style="display:flex;gap:4px;margin-bottom:14px"><span class="num">2</span><span style="border-left:1px solid var(--red)"></span><span class="t">Lorem ipsum dolor sit amet,<br>consectetur adipiscing elit</span></div>
    <div style="display:flex;gap:4px"><span class="num">3</span><span style="border-left:1px solid var(--red)"></span><span class="t">Lorem ipsum dolor sit amet,<br>consectetur adipiscing elit</span></div>
  </div>
  <div class="abs" style="left:118px;top:30px;width:90px">
    <div style="display:flex;gap:4px;margin-bottom:14px"><span class="num">4</span><span style="border-left:1px solid var(--red)"></span><span class="t">Lorem ipsum dolor sit amet,<br>consectetur adipiscing elit</span></div>
    <div style="display:flex;gap:4px;margin-bottom:14px"><span class="num">5</span><span style="border-left:1px solid var(--red)"></span><span class="t">Lorem ipsum dolor sit amet,<br>consectetur adipiscing elit</span></div>
    <div style="display:flex;gap:4px"><span class="num">6</span><span style="border-left:1px solid var(--red)"></span><span class="t">Lorem ipsum dolor sit amet,<br>consectetur adipiscing elit</span></div>
  </div>
  <div class="foot">VANGUARD HONOR LEADERSHIP<span class="pg">Page 7</span></div>
</section>

<section class="slide">
  <div class="ph" style="left:0;top:0;bottom:5px;width:113px;background:linear-gradient(#cfcfcf,#7b7b7b 60%,#2b2b2b)" role="img" aria-label="Laptop on a desk before a city skyline"></div>
  <div class="ttl">Agenda</div>
  <div class="abs" style="left:113px;top:0;right:0;bottom:5px;background:var(--black)"></div>
  <div class="mark light">VANGUARD HONOR</div>
  <div class="abs" style="left:122px;top:20px;width:90px">
    <div style="display:flex;gap:6px;align-items:center;height:20px;border-bottom:.5px solid #444"><span class="num" style="color:#fff">1</span><span class="t" style="color:#ccc">Lorem ipsum dolor sit amet,<br>consectetur adipiscing elit</span></div>
    <div style="display:flex;gap:6px;align-items:center;height:20px;border-bottom:.5px solid #444"><span class="num" style="color:#fff">2</span><span class="t" style="color:#ccc">Lorem ipsum dolor sit amet,<br>consectetur adipiscing elit</span></div>
    <div style="display:flex;gap:6px;align-items:center;height:20px;border-bottom:.5px solid #444"><span class="num" style="color:#fff">3</span><span class="t" style="color:#ccc">Lorem ipsum dolor sit amet,<br>consectetur adipiscing elit</span></div>
    <div style="display:flex;gap:6px;align-items:center;height:20px;border-bottom:.5px solid #444"><span class="num" style="color:#fff">4</span><span class="t" style="color:#ccc">Lorem ipsum dolor sit amet,<br>consectetur adipiscing elit</span></div>
    <div style="display:flex;gap:6px;align-items:center;height:20px"><span class="num" style="color:#fff">5</span><span class="t" style="color:#ccc">Lorem ipsum dolor sit amet,<br>consectetur adipiscing elit</span></div>
  </div>
  <div class="foot">VANGUARD HONOR LEADERSHIP<span class="pg">Page 8</span></div>
</section>

<section class="slide dark">
  <div class="ph" style="left:0;top:0;bottom:5px;width:80px;background:linear-gradient(90deg,#2a2a2a,#0b0b0b)" role="img" aria-label="Uniformed officer in dress blues"></div>
  <div class="ttl" style="left:75px;color:#fff">About Us</div><div class="mark">VANGUARD HONOR</div>
  <div class="t abs" style="left:75px;top:38px;width:118px">Lorem ipsum dolor sit amet, consectetur adipiscing elit, sed do eiusmod tempor incididunt ut labore et dolore magna aliqua. Ut enim ad minim veniam, quis nostrud exercitation ullamco laboris nisi ut aliquip ex ea commodo consequat.<br>Duis aute irure dolor in reprehenderit in voluptate velit esse cillum dolore eu fugiat nulla pariatur. Excepteur sint occaecat cupidatat non proident, sunt in culpa qui officia deserunt mollit anim id est laborum.</div>
  <div class="foot">VANGUARD HONOR LEADERSHIP<span class="pg">Page 9</span></div>
</section>

<section class="slide dark">
  <div class="ph" style="left:0;top:0;bottom:5px;width:75px;background:linear-gradient(90deg,#303030,#0b0b0b)" role="img" aria-label="Executive in a dark suit"></div>
  <div class="ttl" style="left:75px;color:#fff">About Us</div><div class="mark">VANGUARD HONOR</div>
  <div class="t abs" style="left:75px;top:28px;width:120px">Lorem ipsum dolor sit amet, consectetur adipiscing elit, sed do eiusmod tempor incididunt ut labore et dolore magna aliqua. Ut enim ad minim veniam, quis nostrud exercitation ullamco laboris nisi ut aliquip ex ea commodo consequat.<br>Duis aute irure dolor in reprehenderit in voluptate velit esse cillum dolore eu fugiat nulla pariatur. Excepteur sint occaecat cupidatat non proident, sunt in culpa qui officia deserunt mollit anim id est laborum.</div>
  <div class="foot">VANGUARD HONOR LEADERSHIP<span class="pg">Page 10</span></div>
</section>

<section class="slide dark">
  <div class="ph" style="inset:0 0 5px 0;background:radial-gradient(ellipse at 40% 90%,#5a3a1a,#1a120a 60%,#0b0b0b)" role="img" aria-label="Soldier silhouetted on a ridge at sunset"></div>
  <div class="ttl" style="color:#fff">Mission, Vision and Values</div><div class="mark">VANGUARD HONOR</div>
  <div class="icon" style="left:72px;top:34px"></div><div class="t abs" style="left:86px;top:34px;width:120px">Our mission is "Developing Entrepreneurial Leaders and Winning the Small Business War."</div>
  <div class="icon" style="left:72px;top:62px"></div><div class="t abs" style="left:86px;top:60px;width:120px">Our vision is to become the premier entrepreneurial leadership development firm in the world by helping business owners successfully start, grow and create wealth through a defined business doctrine.</div>
  <div class="icon" style="left:72px;top:92px"></div><div class="t abs" style="left:86px;top:90px;width:120px">Our values are embodied by our name - Vanguard Honor - meaning "Always Faithful." Our values are those of the Kestrel Valor Regiment: Honor, Courage &amp; Commitment.</div>
  <div class="foot">VANGUARD HONOR LEADERSHIP<span class="pg">Page 11</span></div>
</section>

<section class="slide dark">
  <div class="ph" style="inset:0 0 5px 0;background:radial-gradient(ellipse at 30% 100%,#3a2712,#0f0b08 60%,#0b0b0b)" role="img" aria-label="Soldier silhouetted at dusk"></div>
  <div class="ttl" style="color:#fff">Mission, Vision and Values</div><div class="mark">VANGUARD HONOR</div>
  <div class="icon" style="left:66px;top:34px;background:#222;border:.5px solid #888"></div><div class="t abs" style="left:86px;top:34px;width:120px">Our mission is "Developing Entrepreneurial Leaders and Winning the Small Business War."</div>
  <div class="sep" style="left:66px;right:14px;top:50px"></div>
  <div class="icon" style="left:66px;top:62px;background:#222;border:.5px solid #888"></div><div class="t abs" style="left:86px;top:58px;width:120px">Our vision is to become the premier entrepreneurial leadership development firm in the world by helping business owners successfully start, grow and create wealth through a defined business doctrine.</div>
  <div class="sep" style="left:66px;right:14px;top:80px"></div>
  <div class="icon" style="left:66px;top:92px;background:#222;border:.5px solid #888"></div><div class="t abs" style="left:86px;top:88px;width:120px">Our values are embodied by our name - Vanguard Honor - meaning "Always Faithful." Our values are those of the Kestrel Valor Regiment: Honor, Courage &amp; Commitment.</div>
  <div class="foot">VANGUARD HONOR LEADERSHIP<span class="pg">Page 12</span></div>
</section>

<section class="slide dark">
  <div class="ph" style="left:0;top:0;bottom:5px;width:95px;background:linear-gradient(#2a2a2a,#5a4a30 55%,#1a140c)" role="img" aria-label="Bronze memorial statue of soldiers raising a flag"></div>
  <div class="ttl" style="color:#fff">Mission, Vision and Values</div><div class="mark">VANGUARD HONOR</div>
  <div class="icon" style="left:100px;top:30px;background:#222;border:.5px solid #888"></div><div class="t abs" style="left:114px;top:28px;width:100px">Our mission is "Developing Entrepreneurial Leaders and Winning the Small Business War."</div>
  <div class="sep" style="left:100px;right:10px;top:48px"></div>
  <div class="icon" style="left:100px;top:62px;background:#222;border:.5px solid #888"></div><div class="t abs" style="left:114px;top:54px;width:100px">Our vision is to become the premier entrepreneurial leadership development firm in the world by helping business owners successfully start, grow and create wealth.</div>
  <div class="sep" style="left:100px;right:10px;top:82px"></div>
  <div class="icon" style="left:100px;top:95px;background:#222;border:.5px solid #888"></div><div class="t abs" style="left:114px;top:88px;width:100px">Our values are embodied by our name - Vanguard Honor. Our values are those of the Kestrel Valor Regiment: Honor, Courage &amp; Commitment.</div>
  <div class="foot">VANGUARD HONOR LEADERSHIP<span class="pg">Page 13</span></div>
</section>

<section class="slide">
  <div class="ttl">Mission, Vision &amp; Values</div><div class="mark">VANGUARD HONOR</div>
  <div class="t abs" style="left:155px;top:9px">Red 8F0508<br>A6B836</div>
  <div class="dot" style="left:46px;top:34px"></div><div class="t abs" style="left:60px;top:33px;width:120px">Our mission is "Developing Entrepreneurial Leaders and Winning the Small Business War."</div>
  <div class="dot" style="left:46px;top:62px"></div><div class="t abs" style="left:60px;top:58px;width:130px">Our vision is to become the premier entrepreneurial leadership development firm in the world by helping business owners successfully start, grow and create wealth through a defined business doctrine.</div>
  <div class="dot" style="left:46px;top:90px"></div><div class="t abs" style="left:60px;top:88px;width:130px">Our values are embodied by our name - Vanguard Honor. Our values are those of the Kestrel Valor Regiment: Honor, Courage &amp; Commitment.</div>
  <div class="foot">VANGUARD HONOR LEADERSHIP<span class="pg">Page 14</span></div>
</section>

<section class="slide">
  <div class="ttl">Mission, Vision &amp; Values</div><div class="mark">VANGUARD HONOR</div>
  <div class="t abs" style="left:158px;top:9px">Red 8F0508</div>
  <div class="dot" style="left:60px;top:34px"></div><div class="t abs" style="left:74px;top:33px;width:120px"><span class="red">Our MISSION</span> is "Developing Entrepreneurial Leaders and Winning the Small Business War."</div>
  <div class="dot" style="left:60px;top:62px"></div><div class="t abs" style="left:74px;top:58px;width:125px"><span class="red">Our VISION</span> is to become the premier entrepreneurial leadership development firm in the world by helping business owners successfully start, grow and create wealth.</div>
  <div class="dot" style="left:60px;top:90px"></div><div class="t abs" style="left:74px;top:88px;width:125px"><span class="red">Our VALUES</span> are embodied by our name - Vanguard Honor. Our values are those of the Kestrel Valor Regiment: Honor, Courage &amp; Commitment.</div>
  <div class="foot">VANGUARD HONOR LEADERSHIP<span class="pg">Page 15</span></div>
</section>

<section class="slide">
  <div class="ttl">Mission, Vision &amp; Values</div><div class="mark">VANGUARD HONOR</div>
  <div class="t abs" style="left:158px;top:9px">Red 8F0508</div>
  <svg class="abs" style="left:18px;top:34px" width="70" height="66" viewBox="0 0 70 66">
    <circle cx="35" cy="20" r="18" fill="#b50d0d" opacity=".95"/>
    <circle cx="22" cy="42" r="18" fill="#0b0b0b" opacity=".9"/>
    <circle cx="48" cy="42" r="18" fill="#a8874f" opacity=".9"/>
    <path d="M32 16 l6 -4 l-2 7 z" fill="#fff"/>
    <circle cx="18" cy="46" r="3" fill="#fff"/>
    <rect x="47" y="42" width="6" height="5" fill="#fff"/>
  </svg>
  <div class="icon" style="left:100px;top:36px;width:7px;height:7px"></div><div class="t abs" style="left:114px;top:35px;width:100px">Our mission is "Developing Entrepreneurial Leaders and Winning the Small Business War."</div>
  <div class="icon" style="left:100px;top:62px;width:7px;height:7px;background:var(--black)"></div><div class="t abs" style="left:114px;top:58px;width:105px">Our vision is to become the premier entrepreneurial leadership development firm in the world by helping business owners successfully start, grow and create wealth.</div>
  <div class="icon" style="left:100px;top:90px;width:7px;height:7px;background:var(--gold)"></div><div class="t abs" style="left:114px;top:86px;width:105px">Our values are embodied by our name - Vanguard Honor. Our values are those of the Kestrel Valor Regiment: Honor, Courage &amp; Commitment.</div>
  <div class="foot">VANGUARD HONOR LEADERSHIP<span class="pg">Page 16</span></div>
</section>

<section class="slide">
  <div class="ttl">Advisory Board</div><div class="mark">VANGUARD HONOR</div>
  <div class="abs" style="left:0;right:0;top:24px;text-align:center;font-size:4px">Vanguard Honor Leadership Institute Advisory Board</div>
  <div class="avatar" style="left:28px;top:40px" role="img" aria-label="Portrait of advisory board member"></div>
  <div class="t abs" style="left:48px;top:40px;width:60px"><span class="red">Major General Thomas R. Hale, KVRD (Ret)</span><br>Commanding General of the 4th Regiment Division</div>
  <div class="avatar" style="left:128px;top:40px" role="img" aria-label="Portrait of advisory board member"></div>
  <div class="t abs" style="left:148px;top:40px;width:60px"><span class="red">Marcus D. Avery</span><br>Founder and Chief Warfighting Officer of the Vanguard Honor Leadership Institute</div>
  <div class="avatar" style="left:28px;top:78px" role="img" aria-label="Portrait of advisory board member"></div>
  <div class="t abs" style="left:48px;top:78px;width:60px"><span class="red">Warren P. Lowell</span><br>High technology industry executive and serial entrepreneur for 40 years</div>
  <div class="avatar" style="left:128px;top:78px" role="img" aria-label="Portrait of advisory board member"></div>
  <div class="t abs" style="left:148px;top:78px;width:60px"><span class="red">Simon T. Brandt</span><br>CEO of Northbridge Growth Partners</div>
  <div class="foot">VANGUARD HONOR LEADERSHIP<span class="pg">Page 17</span></div>
</section>

<section class="slide">
  <div class="ttl">Product and Services</div><div class="mark">VANGUARD HONOR</div>
  <div class="t abs" style="left:18px;top:40px;width:62px"><span class="red">Small business consulting</span><br>Vanguard Honor Leadership works with entrepreneurs and small business owners to develop leaders within your company.</div>
  <div class="t abs" style="left:18px;top:80px;width:62px"><span class="red">Books</span><br>Leadership is learned. This book quantifies the key behaviors needed to reach that goal.</div>
  <svg class="abs" style="left:85px;top:36px" width="62" height="62" viewBox="0 0 62 62">
    <circle cx="31" cy="31" r="22" fill="#b50d0d"/>
    <circle cx="31" cy="31" r="12" fill="#fff"/>
    <circle cx="31" cy="12" r="8" fill="#a8874f" stroke="#fff" stroke-width="1.5"/>
    <circle cx="50" cy="31" r="8" fill="#a8874f" stroke="#fff" stroke-width="1.5"/>
    <circle cx="31" cy="50" r="8" fill="#a8874f" stroke="#fff" stroke-width="1.5"/>
    <circle cx="12" cy="31" r="8" fill="#a8874f" stroke="#fff" stroke-width="1.5"/>
  </svg>
  <div class="t abs" style="left:155px;top:40px;width:62px"><span class="red">Capital</span><br>You can have the greatest products and services, greatest leadership, a wealth creation doctrine.</div>
  <div class="t abs" style="left:155px;top:76px;width:62px"><span class="red">Field Pocket Coach 365</span><br>In the Kestrel Valor Regiment, the pocket training is a teachable moment, with 365 daily modules.</div>
  <div class="foot">VANGUARD HONOR LEADERSHIP<span class="pg">Page 18</span></div>
</section>

<section class="slide">
  <div class="ttl">Product and Services</div><div class="mark">VANGUARD HONOR</div>
  <div class="icon" style="left:20px;top:30px;width:7px;height:7px"></div><div class="t abs" style="left:32px;top:30px;width:75px"><span class="red">Small business consulting</span><br>Vanguard Honor Leadership works with entrepreneurs and small business owners to develop leaders within your company.</div>
  <div class="icon" style="left:118px;top:30px;width:7px;height:7px;background:var(--black)"></div><div class="t abs" style="left:130px;top:30px;width:80px">Capital<br>You can have the greatest products and services, greatest leadership, a wealth creation doctrine.</div>
  <div class="icon" style="left:20px;top:74px;width:7px;height:7px;background:var(--black)"></div><div class="t abs" style="left:32px;top:74px;width:75px">Books<br>Leadership is learned. This book quantifies the key behaviors needed to reach that goal.</div>
  <div class="icon" style="left:118px;top:74px;width:7px;height:7px"></div><div class="t abs" style="left:130px;top:74px;width:80px"><span class="red">Field Pocket Coach 365</span><br>In the Kestrel Valor Regiment, pocket training is a teachable moment with 365 modules.</div>
  <div class="foot">VANGUARD HONOR LEADERSHIP<span class="pg">Page 19</span></div>
</section>

<section class="slide">
  <div class="ttl">Product and Services</div><div class="mark">VANGUARD HONOR</div>
  <div class="icon" style="left:24px;top:28px;width:7px;height:7px"></div><div class="t abs" style="left:36px;top:27px;width:170px"><span class="red">Small business consulting</span><br>Vanguard Honor Leadership works with entrepreneurs and small business owners to develop leaders within your company.</div>
  <div class="icon" style="left:24px;top:50px;width:7px;height:7px;background:var(--black)"></div><div class="t abs" style="left:36px;top:49px;width:170px">Capital<br>You can have the greatest products and services, greatest leadership, a wealth creation doctrine and still lose.</div>
  <div class="icon" style="left:24px;top:72px;width:7px;height:7px"></div><div class="t abs" style="left:36px;top:71px;width:170px"><span class="red">Books</span><br>Leadership is learned. This book quantifies the key behaviors needed to reach that goal.</div>
  <div class="icon" style="left:24px;top:94px;width:7px;height:7px;background:var(--black)"></div><div class="t abs" style="left:36px;top:93px;width:170px">Field Pocket Coach 365<br>In the Kestrel Valor Regiment, pocket training is a teachable moment with 365 daily modules.</div>
  <div class="foot">VANGUARD HONOR LEADERSHIP<span class="pg">Page 20</span></div>
</section>

<section class="slide">
  <div class="ttl">Table</div><div class="mark">VANGUARD HONOR</div>
  <div class="price" style="left:24px;top:30px"><div class="top">$111</div><div class="lab">LOREM IPSUM</div><div class="body t">Vanguard Honor Leadership works with entrepreneurs and small business owners to develop leaders within your company.</div></div>
  <div class="price" style="left:72px;top:30px"><div class="top">$111</div><div class="lab">LOREM IPSUM</div><div class="body t">Vanguard Honor Leadership works with entrepreneurs and small business owners to develop leaders within your company.</div></div>
  <div class="price" style="left:120px;top:30px"><div class="top">$111</div><div class="lab">LOREM IPSUM</div><div class="body t">Vanguard Honor Leadership works with entrepreneurs and small business owners to develop leaders within your company.</div></div>
  <div class="price" style="left:168px;top:30px"><div class="top">$111</div><div class="lab">LOREM IPSUM</div><div class="body t">Vanguard Honor Leadership works with entrepreneurs and small business owners to develop leaders within your company.</div></div>
  <div class="foot">VANGUARD HONOR LEADERSHIP<span class="pg">Page 21</span></div>
</section>

<section class="slide">
  <div class="ttl">Timeline History</div><div class="mark">VANGUARD HONOR</div>
  <svg class="abs" style="left:0;top:55px" width="227" height="20" viewBox="0 0 227 20">
    <line x1="4" y1="10" x2="222" y2="10" stroke="#0b0b0b" stroke-width="1"/>
    <path d="M218 7 L224 10 L218 13 z" fill="#0b0b0b"/>
    <g fill="#555"><circle cx="33" cy="10" r="3.5"/><circle cx="73" cy="10" r="3.5"/><circle cx="113" cy="10" r="3.5"/><circle cx="153" cy="10" r="3.5"/><circle cx="193" cy="10" r="3.5"/></g>
  </svg>
  <div class="abs red" style="left:26px;top:77px;font-size:5px">2014</div>
  <div class="abs red" style="left:66px;top:46px;font-size:5px">2015</div>
  <div class="abs red" style="left:106px;top:77px;font-size:5px">2016</div>
  <div class="abs red" style="left:146px;top:46px;font-size:5px">2017</div>
  <div class="abs red" style="left:186px;top:77px;font-size:5px">2018</div>
  <div class="t abs" style="left:14px;top:22px;width:50px;text-align:center">Lorem ipsum dolor sit amet, consectetur adipiscing elit, sed do tempor incididunt.</div>
  <div class="t abs" style="left:88px;top:22px;width:50px;text-align:center">Lorem ipsum dolor sit amet, consectetur adipiscing elit, sed do tempor incididunt.</div>
  <div class="t abs" style="left:164px;top:22px;width:50px;text-align:center">Lorem ipsum dolor sit amet, consectetur adipiscing elit, sed do tempor incididunt.</div>
  <div class="t abs" style="left:48px;top:93px;width:50px;text-align:center">Lorem ipsum dolor sit amet, consectetur adipiscing elit, sed do tempor incididunt.</div>
  <div class="t abs" style="left:126px;top:93px;width:50px;text-align:center">Lorem ipsum dolor sit amet, consectetur adipiscing elit, sed do tempor incididunt.</div>
  <div class="foot">VANGUARD HONOR LEADERSHIP<span class="pg">Page 22</span></div>
</section>

<section class="slide">
  <div class="ttl">Column Text</div><div class="mark">VANGUARD HONOR</div>
  <div class="abs red" style="left:24px;top:22px;font-size:5px">Lorem ipsum dolor sit amet, consectetur adipiscing elit</div>
  <div class="t abs" style="left:24px;top:36px;width:56px">Lorem ipsum dolor sit amet, consectetur adipiscing elit, sed do eiusmod tempor incididunt ut labore et dolore magna aliqua. Ut enim ad minim veniam, quis nostrud exercitation ullamco laboris nisi ut aliquip.<br>Duis aute irure dolor in reprehenderit in voluptate velit esse cillum dolore eu fugiat nulla pariatur.</div>
  <div class="t abs" style="left:88px;top:36px;width:56px">Lorem ipsum dolor sit amet, consectetur adipiscing elit, sed do eiusmod tempor incididunt ut labore et dolore magna aliqua. Ut enim ad minim veniam, quis nostrud exercitation ullamco laboris nisi ut aliquip.<br>Duis aute irure dolor in reprehenderit in voluptate velit esse cillum dolore eu fugiat nulla pariatur.</div>
  <div class="t abs" style="left:152px;top:36px;width:56px">Lorem ipsum dolor sit amet, consectetur adipiscing elit, sed do eiusmod tempor incididunt ut labore et dolore magna aliqua. Ut enim ad minim veniam, quis nostrud exercitation ullamco laboris nisi ut aliquip.<br>Duis aute irure dolor in reprehenderit in voluptate velit esse cillum dolore eu fugiat nulla pariatur.</div>
  <div class="foot">VANGUARD HONOR LEADERSHIP<span class="pg">Page 23</span></div>
</section>

<section class="slide">
  <div class="ttl">Column Text</div><div class="mark">VANGUARD HONOR</div>
  <div class="abs" style="left:32px;top:30px;width:160px;background:var(--red);color:#fff;padding:2px 3px;font-size:3.4px;line-height:1.35">Lorem ipsum dolor sit amet, consectetur adipiscing elit, sed do eiusmod tempor incididunt ut labore et dolore magna aliqua. Ut enim ad minim veniam, quis nostrud exercitation ullamco laboris nisi ut aliquip.</div>
  <div class="t abs" style="left:32px;top:52px;width:75px">Lorem ipsum dolor sit amet, consectetur adipiscing elit, sed do eiusmod tempor incididunt ut labore et dolore magna aliqua. Ut enim ad minim veniam, quis nostrud exercitation.<br>Duis aute irure dolor in reprehenderit in voluptate velit esse cillum dolore eu fugiat nulla pariatur. Excepteur sint occaecat cupidatat.</div>
  <div class="t abs" style="left:117px;top:52px;width:75px">Lorem ipsum dolor sit amet, consectetur adipiscing elit, sed do eiusmod tempor incididunt ut labore et dolore magna aliqua. Ut enim ad minim veniam, quis nostrud exercitation.<br>Duis aute irure dolor in reprehenderit in voluptate velit esse cillum dolore eu fugiat nulla pariatur. Excepteur sint occaecat cupidatat.</div>
  <div class="foot">VANGUARD HONOR LEADERSHIP<span class="pg">Page 24</span></div>
</section>

<section class="slide">
  <div class="ttl">Column Text</div><div class="mark">VANGUARD HONOR</div>
  <div class="abs red" style="left:24px;top:22px;font-size:5px">Lorem ipsum dolor sit amet, consectetur adipiscing elit</div>
  <div class="t abs" style="left:24px;top:34px;width:185px">Lorem ipsum dolor sit amet, consectetur adipiscing elit, sed do eiusmod tempor incididunt ut labore et dolore magna aliqua. Ut enim ad minim veniam, quis nostrud exercitation ullamco laboris nisi ut aliquip ex ea commodo consequat.<br><br>Duis aute irure dolor in reprehenderit in voluptate velit esse cillum dolore eu fugiat nulla pariatur. Excepteur sint occaecat cupidatat non proident, sunt in culpa qui officia deserunt mollit anim id est laborum.<br><br>Lorem ipsum dolor sit amet, consectetur adipiscing elit, sed do eiusmod tempor incididunt ut labore et dolore magna aliqua. Ut enim ad minim veniam, quis nostrud exercitation ullamco laboris nisi.<br><br>Duis aute irure dolor in reprehenderit in voluptate velit esse cillum dolore eu fugiat nulla pariatur.</div>
  <div class="foot">VANGUARD HONOR LEADERSHIP<span class="pg">Page 25</span></div>
</section>

<section class="slide">
  <div class="ttl">Editable Chart</div><div class="mark">VANGUARD HONOR</div>
  <div class="abs" style="left:14px;top:32px;width:60px;height:60px;border-radius:50%;background:conic-gradient(var(--black) 0 25%,var(--red) 25% 65%,var(--gold) 65% 100%)"></div>
  <div class="abs" style="left:29px;top:47px;width:30px;height:30px;border-radius:50%;background:#fff"></div>
  <div class="abs" style="left:50px;top:36px;font-size:4px;color:#fff">25%</div>
  <div class="abs" style="left:60px;top:72px;font-size:4px;color:#fff">40%</div>
  <div class="abs" style="left:16px;top:58px;font-size:4px;color:#fff">35%</div>
  <div class="dot" style="left:102px;top:38px;width:8px;height:8px"></div><div class="t abs" style="left:116px;top:36px;width:95px">Lorem ipsum dolor sit amet, consectetur adipiscing elit, sed do eiusmod tempor incididunt ut labore.</div>
  <div class="dot" style="left:102px;top:58px;width:8px;height:8px;background:var(--gold)"></div><div class="t abs" style="left:116px;top:56px;width:95px">Lorem ipsum dolor sit amet, consectetur adipiscing elit, sed do eiusmod tempor incididunt ut labore.</div>
  <div class="dot" style="left:102px;top:78px;width:8px;height:8px;background:var(--black)"></div><div class="t abs" style="left:116px;top:76px;width:95px">Lorem ipsum dolor sit amet, consectetur adipiscing elit, sed do eiusmod tempor incididunt ut labore.</div>
  <div class="foot">VANGUARD HONOR LEADERSHIP<span class="pg">Page 26</span></div>
</section>

<section class="slide">
  <div class="ttl">Editable Chart</div><div class="mark">VANGUARD HONOR</div>
  <svg class="abs" style="left:16px;top:22px" width="200" height="68" viewBox="0 0 200 68">
    <g font-size="3" fill="#555" font-family="Arimo, Arial, sans-serif">
      <text x="0" y="4">40</text><text x="0" y="22">30</text><text x="0" y="40">20</text><text x="0" y="58">10</text>
      <text x="14" y="66">January</text><text x="50" y="66">February</text><text x="90" y="66">March</text><text x="128" y="66">April</text><text x="166" y="66">May</text>
    </g>
    <line x1="8" y1="61" x2="196" y2="61" stroke="#999" stroke-width=".4"/>
    <rect x="14" y="30" width="5" height="31" fill="#0b0b0b"/><rect x="19" y="40" width="5" height="21" fill="#b50d0d"/><rect x="24" y="34" width="5" height="27" fill="#a8874f"/>
    <rect x="52" y="20" width="5" height="41" fill="#0b0b0b"/><rect x="57" y="24" width="5" height="37" fill="#b50d0d"/><rect x="62" y="44" width="5" height="17" fill="#a8874f"/>
    <rect x="90" y="10" width="5" height="51" fill="#0b0b0b"/><rect x="95" y="36" width="5" height="25" fill="#b50d0d"/><rect x="100" y="46" width="5" height="15" fill="#a8874f"/>
    <rect x="128" y="26" width="5" height="35" fill="#0b0b0b"/><rect x="133" y="30" width="5" height="31" fill="#b50d0d"/><rect x="138" y="32" width="5" height="29" fill="#a8874f"/>
    <rect x="166" y="30" width="5" height="31" fill="#0b0b0b"/><rect x="171" y="36" width="5" height="25" fill="#b50d0d"/><rect x="176" y="18" width="5" height="43" fill="#a8874f"/>
  </svg>
  <div class="abs t" style="left:36px;top:94px;line-height:1.9"><span style="display:inline-block;width:4px;height:4px;background:var(--black)"></span> Information Information Information<br><span style="display:inline-block;width:4px;height:4px;background:var(--red)"></span> Information Information Information<br><span style="display:inline-block;width:4px;height:4px;background:var(--gold)"></span> Information Information Information</div>
  <div class="t abs" style="left:124px;top:96px;width:80px">Lorem ipsum dolor sit amet, consectetur adipiscing elit, sed do eiusmod tempor incididunt ut labore et dolore magna aliqua.</div>
  <div class="foot">VANGUARD HONOR LEADERSHIP<span class="pg">Page 27</span></div>
</section>

<section class="slide">
  <div class="ttl">Editable Chart</div><div class="mark">VANGUARD HONOR</div>
  <svg class="abs" style="left:20px;top:20px" width="200" height="64" viewBox="0 0 200 64">
    <g font-size="3" fill="#555" font-family="Arimo, Arial, sans-serif"><text x="0" y="8">April</text><text x="0" y="22">March</text><text x="0" y="37">February</text><text x="0" y="52">January</text></g>
    <line x1="22" y1="0" x2="22" y2="58" stroke="#999" stroke-width=".4"/>
    <rect x="22" y="3" width="60" height="2.5" fill="#0b0b0b"/><rect x="22" y="5.5" width="70" height="2.5" fill="#b50d0d"/><rect x="22" y="8" width="40" height="2.5" fill="#a8874f"/>
    <rect x="22" y="17" width="110" height="2.5" fill="#0b0b0b"/><rect x="22" y="19.5" width="80" height="2.5" fill="#b50d0d"/><rect x="22" y="22" width="50" height="2.5" fill="#a8874f"/>
    <rect x="22" y="32" width="95" height="2.5" fill="#0b0b0b"/><rect x="22" y="34.5" width="70" height="2.5" fill="#b50d0d"/><rect x="22" y="37" width="55" height="2.5" fill="#a8874f"/>
    <rect x="22" y="47" width="120" height="2.5" fill="#0b0b0b"/><rect x="22" y="49.5" width="90" height="2.5" fill="#b50d0d"/><rect x="22" y="52" width="65" height="2.5" fill="#a8874f"/>
    <g font-size="2.6" fill="#777" font-family="Arimo, Arial, sans-serif"><text x="22" y="63">0</text><text x="52" y="63">10</text><text x="82" y="63">20</text><text x="112" y="63">30</text><text x="142" y="63">40</text><text x="172" y="63">50</text></g>
  </svg>
  <div class="abs t" style="left:36px;top:92px;line-height:1.9"><span style="display:inline-block;width:4px;height:4px;background:var(--black)"></span> Information Information<br><span style="display:inline-block;width:4px;height:4px;background:var(--red)"></span> Information Information<br><span style="display:inline-block;width:4px;height:4px;background:var(--gold)"></span> Information Information</div>
  <div class="t abs" style="left:124px;top:94px;width:80px">Lorem ipsum dolor sit amet, consectetur adipiscing elit, sed do eiusmod tempor incididunt ut labore et dolore magna aliqua.</div>
  <div class="foot">VANGUARD HONOR LEADERSHIP<span class="pg">Page 28</span></div>
</section>

<section class="slide">
  <div class="ttl">Editable Chart</div><div class="mark">VANGUARD HONOR</div>
  <div class="abs red" style="left:24px;top:24px;font-size:5px">Lorem ipsum dolor sit amet, consectetur adipiscing elit</div>
  <div class="t abs" style="left:24px;top:34px;width:180px">Lorem ipsum dolor sit amet, consectetur adipiscing elit, sed do eiusmod tempor incididunt ut labore et dolore magna aliqua. Ut enim ad minim veniam, quis nostrud exercitation ullamco laboris nisi ut aliquip.</div>
  <svg class="abs" style="left:0;top:52px" width="227" height="71" viewBox="0 0 227 71">
    <rect width="227" height="71" fill="#0b0b0b"/>
    <g stroke="#333" stroke-width=".4"><line x1="18" y1="10" x2="220" y2="10"/><line x1="18" y1="25" x2="220" y2="25"/><line x1="18" y1="40" x2="220" y2="40"/><line x1="18" y1="55" x2="220" y2="55"/></g>
    <path d="M18 64 L40 58 L70 50 L100 44 L125 40 L140 20 L150 10 L160 30 L175 45 L195 55 L220 58 L220 64 Z" fill="#a8874f"/>
    <path d="M18 64 L40 60 L70 56 L100 52 L120 44 L135 30 L150 22 L165 42 L185 52 L200 50 L220 60 L220 64 Z" fill="#b50d0d"/>
    <g font-size="3" fill="#bbb" font-family="Arimo, Arial, sans-serif"><text x="4" y="12">160</text><text x="4" y="27">120</text><text x="6" y="42">80</text><text x="6" y="57">40</text>
    <text x="18" y="69">01/01/2018</text><text x="70" y="69">08/01/2018</text><text x="120" y="69">15/01/2018</text><text x="160" y="69">22/01/2018</text><text x="196" y="69">29/01/2018</text></g>
  </svg>
  <div class="foot">VANGUARD HONOR LEADERSHIP<span class="pg">Page 29</span></div>
</section>

<section class="slide">
  <div class="ttl">Editable Chart</div><div class="mark">VANGUARD HONOR</div>
  <svg class="abs" style="left:10px;top:34px" width="150" height="64" viewBox="0 0 150 64">
    <g font-size="3.2" fill="#555" font-family="Arimo, Arial, sans-serif"><text x="0" y="5">137,5</text><text x="2" y="16">110</text><text x="1" y="27">82,5</text><text x="4" y="38">55</text><text x="1" y="49">27,5</text><text x="6" y="58">0</text>
    <text x="16" y="63">April</text><text x="38" y="63">May</text><text x="60" y="63">June</text><text x="82" y="63">July</text><text x="104" y="63">Aug</text><text x="126" y="63">Sept</text></g>
    <line x1="14" y1="56" x2="146" y2="56" stroke="#999" stroke-width=".4"/>
    <polyline points="18,50 40,44 62,36 84,24 106,18 128,24" fill="none" stroke="#0b0b0b" stroke-width=".8"/>
    <polyline points="18,36 40,40 62,34 84,38 106,34 128,36" fill="none" stroke="#b50d0d" stroke-width=".8"/>
    <g fill="#0b0b0b"><circle cx="18" cy="50" r="1"/><circle cx="40" cy="44" r="1"/><circle cx="62" cy="36" r="1"/><circle cx="84" cy="24" r="1"/><circle cx="106" cy="18" r="1"/><circle cx="128" cy="24" r="1"/></g>
    <g fill="#b50d0d"><circle cx="18" cy="36" r="1"/><circle cx="40" cy="40" r="1"/><circle cx="62" cy="34" r="1"/><circle cx="84" cy="38" r="1"/><circle cx="106" cy="34" r="1"/><circle cx="128" cy="36" r="1"/></g>
  </svg>
  <div class="t abs" style="left:166px;top:38px;width:52px">Lorem ipsum dolor sit amet, consectetur adipiscing elit, sed do eiusmod tempor incididunt ut labore et dolore magna aliqua.</div>
  <div class="t abs" style="left:166px;top:62px;width:52px">Lorem ipsum dolor sit amet, consectetur adipiscing elit, sed do eiusmod tempor incididunt ut labore et dolore magna aliqua.</div>
  <div class="foot">VANGUARD HONOR LEADERSHIP<span class="pg">Page 30</span></div>
</section>

<section class="slide">
  <div class="ttl">Slide with image</div><div class="mark">VANGUARD HONOR</div>
  <div class="ph" style="left:0;right:0;top:20px;height:62px;background:linear-gradient(90deg,#e6e1d8,#bdb7ac 50%,#d8d2c8)" role="img" aria-label="Desk with newspaper, laptop, phone and coffee"></div>
  <div class="abs" style="left:50px;top:77px;width:12px;height:12px;background:var(--black)"></div>
  <div class="abs" style="left:108px;top:77px;width:12px;height:12px;background:var(--red)"></div>
  <div class="abs" style="left:166px;top:77px;width:12px;height:12px;background:var(--gold)"></div>
  <div class="t abs" style="left:28px;top:93px;width:55px;text-align:center">Lorem ipsum dolor sit amet, consectetur adipiscing elit, sed do eiusmod tempor incididunt ut labore.</div>
  <div class="t abs" style="left:86px;top:93px;width:55px;text-align:center">Lorem ipsum dolor sit amet, consectetur adipiscing elit, sed do eiusmod tempor incididunt ut labore.</div>
  <div class="t abs" style="left:144px;top:93px;width:55px;text-align:center">Lorem ipsum dolor sit amet, consectetur adipiscing elit, sed do eiusmod tempor incididunt ut labore.</div>
  <div class="foot">VANGUARD HONOR LEADERSHIP<span class="pg">Page 31</span></div>
</section>

<section class="slide">
  <div class="ttl">Slide with image</div><div class="mark">VANGUARD HONOR</div>
  <div class="ph" style="left:0;right:0;top:20px;bottom:5px;background:linear-gradient(90deg,#2e2a26,#7a6e62 55%,#d8d2cc)" role="img" aria-label="Modern conference room with long table and windows"></div>
  <div class="abs" style="left:22px;top:30px;width:44px;height:80px;background:var(--black)"></div>
  <div class="t abs" style="left:26px;top:36px;width:36px;color:#ddd">Lorem ipsum dolor sit amet, consectetur adipiscing elit, sed do eiusmod tempor incididunt ut labore et dolore magna aliqua.</div>
  <div class="foot">VANGUARD HONOR LEADERSHIP<span class="pg">Page 32</span></div>
</section>

<section class="slide">
  <div class="ttl">Slide with image</div><div class="mark">VANGUARD HONOR</div>
  <div class="ph" style="left:10px;top:24px;width:50px;height:34px;background:linear-gradient(#a9a9a9,#5a5a5a)" role="img" aria-label="Business team in a meeting"></div>
  <div class="abs" style="left:60px;top:24px;width:24px;height:34px;background:var(--red)"></div>
  <div class="ph" style="left:10px;top:58px;width:74px;height:40px;background:linear-gradient(#6b6b6b,#2a2a2a)" role="img" aria-label="Colleagues reviewing documents together"></div>
  <div class="ph" style="left:84px;top:24px;width:60px;height:50px;background:linear-gradient(#8c8c8c,#3a3a3a)" role="img" aria-label="Executives discussing around a table"></div>
  <div class="abs red" style="left:152px;top:26px;font-size:4.5px">LOREM IPSUM</div>
  <div class="t abs" style="left:152px;top:34px;width:65px">Lorem ipsum dolor sit amet, consectetur adipiscing elit, sed do eiusmod tempor incididunt ut labore et dolore magna aliqua. Ut enim ad minim veniam, quis nostrud exercitation ullamco laboris nisi ut aliquip ex ea commodo consequat.<br>Duis aute irure dolor in reprehenderit in voluptate velit esse cillum dolore eu fugiat nulla pariatur. Excepteur sint occaecat.</div>
  <div class="foot">VANGUARD HONOR LEADERSHIP<span class="pg">Page 33</span></div>
</section>

<section class="slide">
  <div class="ttl">Slide with image</div><div class="mark">VANGUARD HONOR</div>
  <div class="ph" style="left:12px;top:24px;width:90px;height:46px;background:linear-gradient(135deg,#1c2a44,#3b4f74)" role="img" aria-label="Businessman touching a digital network display"></div>
  <div class="abs" style="left:110px;top:24px;width:90px;height:30px;background:var(--red)"></div>
  <div class="t abs" style="left:116px;top:28px;width:78px;color:#fff">Lorem ipsum dolor sit amet, consectetur adipiscing elit, sed do eiusmod tempor incididunt ut labore et dolore magna aliqua.</div>
  <div class="abs" style="left:12px;top:74px;width:90px;height:42px;background:var(--black)"></div>
  <div class="t abs" style="left:18px;top:90px;width:78px;color:#ddd">Lorem ipsum dolor sit amet, consectetur adipiscing elit, sed do eiusmod tempor incididunt ut labore et dolore magna aliqua.</div>
  <div class="ph" style="left:110px;top:58px;width:90px;height:58px;background:linear-gradient(135deg,#1f3c6a,#4d7fb8)" role="img" aria-label="Connected network of people icons"></div>
  <div class="foot">VANGUARD HONOR LEADERSHIP<span class="pg">Page 34</span></div>
</section>

<section class="slide dark" style="background:#121212">
  <div class="abs" style="left:0;right:0;top:30px;text-align:center;font-size:9px">CONTACT US</div>
  <div class="abs" style="left:0;right:0;top:44px;text-align:center;font-size:4px;color:#ddd">Vanguard Honor Leadership Institute</div>
  <div class="t abs" style="left:82px;top:56px;line-height:2;color:#ddd">
    <div><span class="red">&#9679;</span>&nbsp; 4100 Ridgeline Way<br>&nbsp;&nbsp;&nbsp; Fairhaven, TX 75900</div>
    <div><svg width="4" height="4" viewBox="0 0 10 10"><path d="M2 1 L4 1 L5 3 L4 4 Q5 6 6 6 L7 5 L9 6 L9 8 Q9 9 8 9 Q1 8 1 2 Q1 1 2 1 Z" fill="#fff"/></svg>&nbsp; 555.014.2288</div>
    <div><svg width="4" height="3" viewBox="0 0 10 7"><rect x="0" y="0" width="10" height="7" fill="#fff"/><path d="M0 0 L5 4 L10 0" fill="none" stroke="#121212" stroke-width="1"/></svg>&nbsp; marcus@vanguardhonor.example</div>
  </div>
</section>

</main>
</body>
</html>
```